Mardi Gras 2013 Design Project

We have a design with elements that we want to retain. However, we need to take what we have and give it a creative BOOST!

Requirements
Must have
• Colors must stay, "KL" logo must stay,
Copy must remain (except - "Requests Your Presence" and small copy in bottom right corner);
Seal must remain, "9th Annual Mardi Gras Ball" frame text can be modified but should resemble;
Gotham font to remain
Nice to have
• Any new Mardi Gras element - like a mask or beads - but can not over shadow copy

```html
<!DOCTYPE html>
<html lang="en">
<head>
<meta charset="utf-8">
<title>9th Annual Mardi Gras Ball</title>
<link rel="stylesheet" href="https://fonts.googleapis.com/css2?family=Montserrat:ital,wght@0,700;0,800;1,700;1,800;1,900&family=Roboto+Condensed:wght@400&display=swap">
<style>
  :root {
    --purple-deep: #6a2fb0;
    --purple-mid: #6d45a9;
    --purple-soft: #7249ad;
    --gold: #f4b117;
    --green: #27a24a;
    --white: #ffffff;
    --ink: #111111;
    --page: #ffffff;
  }
  html, body {
    margin: 0;
    padding: 0;
    width: 1000px;
    height: 1200px;
    overflow: hidden;
    background: var(--page);
  }
  .canvas {
    position: relative;
    width: 1000px;
    height: 1200px;
    font-family: "Montserrat", sans-serif;
  }
  .artwork { position: absolute; left: 0; top: 0; }
  .copy { position: absolute; margin: 0; font-style: italic; font-weight: 800; line-height: 1; white-space: nowrap; }

  .host { left: 405px; top: 256px; font-size: 22px; line-height: 1.3; color: var(--gold); }

  .edition { left: 612px; top: 372px; color: var(--white); font-weight: 900;
    -webkit-text-stroke: 3px var(--ink); paint-order: stroke fill;
    text-shadow: 4px 4px 0 var(--ink); }
  .edition .num { font-size: 98px; }
  .edition .suffix { font-size: 54px; vertical-align: 30px; }

  .annual { left: 494px; top: 474px; font-size: 50px; color: var(--white);
    -webkit-text-stroke: 3px var(--gold); paint-order: stroke fill;
    text-shadow: 3px 3px 0 var(--ink); }

  .title-line { font-size: 82px; font-weight: 900; color: var(--white); paint-order: stroke fill; }
  .title-mardi { left: 408px; top: 530px; -webkit-text-stroke: 5px var(--purple-deep); text-shadow: 4px 4px 0 var(--ink); }
  .title-gras { left: 440px; top: 610px; -webkit-text-stroke: 5px var(--green); text-shadow: 4px 4px 0 var(--ink); }
  .title-ball { left: 416px; top: 690px; font-size: 86px; -webkit-text-stroke: 5px var(--gold); text-shadow: 4px 4px 0 var(--ink); }

  .day { left: 413px; top: 818px; font-size: 35px; color: var(--gold); }
  .date { left: 335px; top: 868px; font-size: 29px; color: var(--green); }
  .time { left: 432px; top: 912px; font-size: 27px; color: var(--white); }

  .venue { left: 250px; top: 1000px; color: var(--gold); text-align: center; width: 228px; }
  .venue-name { display: block; font-size: 16px; line-height: 1.3; }
  .venue-street { display: block; font-family: "Roboto Condensed", sans-serif; font-style: normal; font-weight: 400;
    font-size: 14px; color: var(--green); margin-top: 4px; }
  .venue-city { display: block; font-size: 20px; color: var(--green); margin-top: 3px; }

  .brand-mark { position: absolute; left: 118px; top: 240px; font-weight: 800; font-style: normal;
    font-size: 130px; color: var(--gold); line-height: 1; letter-spacing: -4px; margin: 0; }

  .seal-name { position: absolute; left: 750px; top: 842px; width: 142px; text-align: center; margin: 0;
    font-weight: 800; font-size: 15px; line-height: 1.25; color: var(--purple-deep); }
</style>
</head>
<body>
<div class="canvas">
  <svg class="artwork" width="1000" height="1200" viewBox="0 0 1000 1200">
    <defs>
      <clipPath id="poster-clip"><rect x="75" y="42" width="850" height="1106"/></clipPath>
      <linearGradient id="photo-mask" x1="0" y1="0" x2="1" y2="1">
        <stop offset="0" stop-color="#1d2a3a"/><stop offset="0.5" stop-color="#5b4aa8"/><stop offset="1" stop-color="#2d3048"/>
      </linearGradient>
      <linearGradient id="photo-beads" x1="0" y1="0" x2="0" y2="1">
        <stop offset="0" stop-color="#c9a64a"/><stop offset="0.5" stop-color="#d8c27a"/><stop offset="1" stop-color="#b88f2c"/>
      </linearGradient>
      <linearGradient id="photo-glitter" x1="0" y1="0" x2="1" y2="1">
        <stop offset="0" stop-color="#b3246e"/><stop offset="0.5" stop-color="#3b7c9a"/><stop offset="1" stop-color="#b48428"/>
      </linearGradient>
      <linearGradient id="photo-harlequin" x1="0" y1="0" x2="1" y2="1">
        <stop offset="0" stop-color="#d9a244"/><stop offset="0.5" stop-color="#c9497a"/><stop offset="1" stop-color="#e0b255"/>
      </linearGradient>
      <filter id="panel-shadow" x="-10%" y="-10%" width="120%" height="120%">
        <feDropShadow dx="0" dy="6" stdDeviation="10" flood-color="#000" flood-opacity="0.45"/>
      </filter>
    </defs>

    <g clip-path="url(#poster-clip)">
      <rect x="75" y="42" width="520" height="320" fill="url(#photo-mask)" role="img" aria-label="Photo of a person wearing a feathered carnival mask"/>
      <rect x="595" y="42" width="330" height="760" fill="url(#photo-beads)" role="img" aria-label="Photo of purple, green and gold Mardi Gras beads with a painted mask"/>
      <rect x="75" y="560" width="380" height="588" fill="url(#photo-glitter)" role="img" aria-label="Photo of a glittering carnival mask and beads"/>
      <rect x="380" y="880" width="545" height="268" fill="url(#photo-harlequin)" role="img" aria-label="Photo of a gold and pink harlequin glitter mask"/>

      <polygon class="panel panel-left" points="75,205 690,40 900,720 75,665" fill="var(--purple-soft)" filter="url(#panel-shadow)"/>
      <polygon class="panel panel-right" points="600,42 705,42 862,256 925,580 925,950 620,900" fill="var(--purple-mid)" filter="url(#panel-shadow)"/>
      <polygon class="panel panel-bottom" points="160,860 925,945 925,962 432,1078 252,1148 200,1148" fill="var(--purple-mid)" filter="url(#panel-shadow)"/>
      <polygon class="panel panel-front" points="398,100 910,262 650,1050 155,862" fill="var(--purple-deep)" filter="url(#panel-shadow)"/>
      <polygon class="panel-edge-band" points="890,268 910,274 652,1050 632,1044" fill="var(--gold)"/>

      <circle class="seal" cx="821" cy="860" r="72" fill="var(--gold)" stroke="var(--purple-deep)" stroke-width="5"/>
    </g>
  </svg>

  <p class="brand-mark">KL</p>
  <p class="seal-name">KINGSLEY<br>LANE</p>

  <p class="copy host">THE ASSOCIATION OF<br>ST KINGSLEY LANE ALUMNI</p>
  <p class="copy edition"><span class="num">9</span><span class="suffix">th</span></p>
  <p class="copy annual">ANNUAL</p>
  <p class="copy title-line title-mardi">MARDI</p>
  <p class="copy title-line title-gras">GRAS</p>
  <p class="copy title-line title-ball">BALL</p>

  <p class="copy day">SATURDAY</p>
  <p class="copy date">JANUARY 26, 2013</p>
  <p class="copy time">7PM - 12AM</p>

  <p class="copy venue">
    <span class="venue-name">LAKEVIEW CIVIC<br>CONVENTION CENTER</span>
    <span class="venue-street">4100 Harbor Hall Drive</span>
    <span class="venue-city">RIVERTON, GEORGIA</span>
  </p>
</div>
</body>
</html>
```